Business card for pediatric occupational therapist

I need a business card design for my independent occupational therapy company. I am a pediatric occupational therapist working with children 0-3 years of age. I would like the card to be clean (not too 'busy') and can include pictures/cartoon-like images of children, or toys such as building blocks, or other images that would be relevant to pediatric therapy. I want it to look professional but also intended to be clear that services provided are for children.
Target Market(s)
Families requiring occupational therapy services for their children (physical, emotional, social needs) - developmental delays
Industry/Entity Type
Rehabilitation
Contact Information for Business Card
Maren Tolsvik OT LLC
Maren Tolsvik, OTR/L
Occupational Therapist
maren.tolsvikOT@brindlemail.com

```html
<!DOCTYPE html>
<html lang="en">
<head>
<meta charset="utf-8">
<title>Maren Tolsvik OT LLC – Business Card</title>
<link rel="stylesheet" href="https://fonts.googleapis.com/css2?family=Lexend:wght@500&family=Nunito+Sans:wght@300;400;900&display=swap">
<style>
  :root {
    --navy: #164a6c;
    --swirl: #5a8fb4;
    --white: #ffffff;
    --backdrop: #e6e6e6;
  }
  * { box-sizing: border-box; margin: 0; padding: 0; }
  html, body { width: 1200px; height: 765px; overflow: hidden; }
  body { background: var(--backdrop); position: relative; font-family: "Nunito Sans", sans-serif; }

  .card {
    position: absolute;
    width: 520px;
    height: 297px;
    border-radius: 24px;
    border: 3px solid var(--white);
    overflow: hidden;
  }

  /* Front face */
  .card-front { left: 290px; top: 64px; background: var(--navy); }
  .swirl-field {
    position: absolute;
    border-radius: 50%;
    background: radial-gradient(circle, rgba(90,143,180,0.35), rgba(90,143,180,0) 70%);
  }
  .swirl-field--top-right { right: -40px; top: -40px; width: 200px; height: 260px; border-radius: 40%; }
  .swirl-field--bottom-left { left: -30px; bottom: -40px; width: 120px; height: 120px; }
  .icon-grid { position: absolute; left: 0; top: 0; }
  .icon-badge {
    position: absolute;
    width: 52px; height: 52px;
    border: 2px solid var(--white);
    border-radius: 50%;
    background: rgba(255,255,255,0.12);
  }
  .front-title {
    position: absolute;
    left: 236px; top: 96px;
    font-family: "Lexend", sans-serif;
    font-weight: 500;
    font-size: 29px;
    line-height: 35px;
    color: var(--white);
  }

  /* Back face */
  .card-back { left: 378px; top: 405px; background: var(--white); }
  .side-band {
    position: absolute; left: 0; top: 0; bottom: 0;
    width: 131px;
    background: var(--navy);
  }
  .side-band .icon-badge { width: 56px; height: 56px; left: 37px; }
  .side-band .swirl-field--band { left: -20px; bottom: -30px; width: 110px; height: 110px; }
  .contact { position: absolute; left: 158px; top: 117px; color: var(--navy); }
  .contact-name { font-size: 27px; line-height: 32px; white-space: nowrap; }
  .contact-name strong { font-weight: 900; }
  .contact-name span { font-weight: 400; }
  .contact-role { font-weight: 300; font-size: 20px; line-height: 26px; }
  .contact-email {
    margin-top: 22px;
    display: flex; align-items: center; gap: 7px;
    font-weight: 400; font-size: 16px;
  }
  .contact-email svg { width: 24px; height: 20px; }
</style>
</head>
<body>

  <section class="card card-front">
    <div class="swirl-field swirl-field--top-right" role="img" aria-label="Decorative light-blue spiral swirls"></div>
    <div class="swirl-field swirl-field--bottom-left" role="img" aria-label="Decorative light-blue spiral swirls"></div>
    <div class="icon-grid">
      <div class="icon-badge" style="left:88px; top:50px;" role="img" aria-label="Pacifier icon"></div>
      <div class="icon-badge" style="left:150px; top:50px;" role="img" aria-label="Stacking rings toy icon"></div>
      <div class="icon-badge" style="left:88px; top:119px;" role="img" aria-label="Baby stroller icon"></div>
      <div class="icon-badge" style="left:150px; top:119px;" role="img" aria-label="Baby onesie icon"></div>
      <div class="icon-badge" style="left:88px; top:189px;" role="img" aria-label="Baby bottle icon"></div>
      <div class="icon-badge" style="left:150px; top:189px;" role="img" aria-label="Baby rattle icon"></div>
    </div>
    <h1 class="front-title">Pediatric<br>Occupational<br>Therapist</h1>
  </section>

  <section class="card card-back">
    <div class="side-band">
      <div class="swirl-field swirl-field--band" role="img" aria-label="Decorative light-blue spiral swirls"></div>
      <div class="icon-badge" style="top:45px;" role="img" aria-label="Pacifier icon"></div>
      <div class="icon-badge" style="top:118px;" role="img" aria-label="Baby stroller icon"></div>
      <div class="icon-badge" style="top:192px;" role="img" aria-label="Baby bottle icon"></div>
    </div>
    <div class="contact">
      <p class="contact-name"><strong>Maren Tolsvik</strong> <span>OT LLC</span></p>
      <p class="contact-role">Occupational Therapist</p>
      <p class="contact-email">
        <svg viewBox="0 0 24 20" aria-hidden="true">
          <rect x="1" y="5" width="22" height="14" rx="1" fill="none" stroke="var(--navy)" stroke-width="1.8"/>
          <path d="M1 6 L12 13 L23 6" fill="none" stroke="var(--navy)" stroke-width="1.8"/>
          <path d="M5 6 V1 H19 V6" fill="none" stroke="var(--navy)" stroke-width="1.5"/>
        </svg>
        maren.tolsvikOT@brindlemail.com
      </p>
    </div>
  </section>

</body>
</html>
```